Dutch psychology podcast needs logo / art design

I need a logo / artwork for my new podcast on psychology/health called 'Het Stille Kompas'. In the podcast I talk to different experts on subjects as personal development, psychology, health, spirituality and entrepreneurship. I would like to see my brand colors back in the design (www.joristeulinghof.nl) and my face in the artwork since I'm the host of the show.

My photo is included in the attachments and I've also added some examples of what I'm looking for.

Industry/Entity Type

Psychology

Colors

Designer to choose colors to be used in the design.

Requirements
Must have
• - Name of the show: 'Het Stille Kompas' (I prefer that this name is turned into a logo), see attachment of example of Harbor of Quiet Minds
• - Subtitle: 'met Joris Teulinghof' which is my name a the host
• - My picture, see attachments

```html
<!DOCTYPE html>
<html lang="nl">
<head>
<meta charset="utf-8">
<title>Het Stille Kompas – podcast artwork</title>
<link rel="stylesheet" href="https://fonts.googleapis.com/css2?family=Oswald:wght@600&family=Poppins:wght@300;700&display=swap">
<style>
  :root {
    --teal-deep: #38ae97;
    --teal-mid: #5fc0ad;
    --teal-light: #b4dfe0;
    --ink-cream: #effdf0;
    --host-top: #6b5646;
    --host-body: #1e2236;
  }
  html, body {
    margin: 0;
    padding: 0;
    width: 1200px;
    height: 1200px;
    overflow: hidden;
    background: var(--teal-deep);
  }
  .cover {
    position: relative;
    width: 1200px;
    height: 1200px;
    background: radial-gradient(circle at 957px 350px, var(--teal-light) 0%, var(--teal-mid) 45%, var(--teal-deep) 85%);
  }
  .cover-art {
    position: absolute;
    inset: 0;
    width: 1200px;
    height: 1200px;
    display: block;
  }
  .frame-line {
    stroke: var(--ink-cream);
    stroke-width: 2.6;
    fill: none;
  }
  .show-kicker {
    font-family: "Oswald", sans-serif;
    font-weight: 600;
    font-size: 92px;
    fill: var(--ink-cream);
  }
  .show-title {
    font-family: "Oswald", sans-serif;
    font-weight: 600;
    font-size: 176px;
    fill: var(--ink-cream);
  }
  .host-line {
    font-family: "Poppins", sans-serif;
    font-weight: 300;
    font-size: 38px;
    fill: var(--ink-cream);
  }
  .host-line .host-first {
    font-weight: 700;
  }
</style>
</head>
<body>
<div class="cover">
  <svg class="cover-art" viewBox="0 0 1200 1200" xmlns="http://www.w3.org/2000/svg">
    <defs>
      <linearGradient id="hostTone" x1="0" y1="0" x2="0" y2="1">
        <stop offset="0" stop-color="var(--host-top)"/>
        <stop offset="0.45" stop-color="#4a3e3a"/>
        <stop offset="0.55" stop-color="var(--host-body)"/>
        <stop offset="1" stop-color="var(--host-body)"/>
      </linearGradient>
    </defs>

    <path class="host-photo" role="img" aria-label="Portretfoto van host Joris Teulinghof, glimlachend met gekruiste armen in een donkerblauwe trui"
      fill="url(#hostTone)"
      d="M380 760 C390 680 440 650 560 610 L640 565 L640 470 C620 420 630 330 650 280 C660 150 720 60 800 60 C880 60 930 140 920 260 C940 330 930 420 905 480 L900 560 C980 600 1060 640 1100 680 C1150 760 1200 900 1200 1000 L1200 1200 L370 1200 Z"/>

    <g class="title-frame">
      <line class="frame-line" x1="45" y1="681" x2="402" y2="681"/>
      <line class="frame-line" x1="798" y1="681" x2="1156" y2="681"/>
      <line class="frame-line" x1="1155" y1="680" x2="1155" y2="1057"/>
      <line class="frame-line" x1="45" y1="680" x2="45" y2="1057"/>
      <line class="frame-line" x1="44" y1="1056" x2="363" y2="1056"/>
      <line class="frame-line" x1="832" y1="1056" x2="1156" y2="1056"/>
    </g>

    <text class="show-kicker" x="593" y="714" text-anchor="middle" textLength="138" lengthAdjust="spacingAndGlyphs">HET</text>
    <text class="show-title" x="87" y="947" textLength="1025" lengthAdjust="spacingAndGlyphs">STILLE KOMPAS</text>
    <text class="host-line" x="388" y="1067" textLength="409" lengthAdjust="spacingAndGlyphs">MET <tspan class="host-first">JORIS</tspan>TEULINGHOF</text>
  </svg>
</div>
</body>
</html>
```